Calm Fern Healthcare- Aged Care and Community Services

Looking for brochure to advertise our services. I will attach a draft that we do not want to use. Looking for graphics that are as natural as possible to present a personalised service. We supply services to aged people and people with disability. Please make it look classy and professional at the same time. I am looking for creativity. I have also attached the logo. Site addresses can be the last page. ideally looking for 2 designs, one A4 and another smaller possibly DL. Looking for creative out of the box thinkers. Thank you.

Target Market(s)

Aged Care service providers, disability service providers and private hospitals

Font styles to use
Serif
Sans Serif
Script

Colors
6b449b
886aae
eea4c8
f59195
fac994
3176b5
0555a3
cedeed
e4daeb

Requirements
Must have
• Targeted imagery, content and contact details
Nice to have
• personal profiles of people happy with our services

```html
<!DOCTYPE html>
<html lang="en">
<head>
<meta charset="utf-8">
<title>Calm Fern Healthcare – Brochure</title>
<link href="https://fonts.googleapis.com/css2?family=Raleway:wght@400;500;600;700&family=Roboto+Condensed:wght@400&family=Great+Vibes&display=swap" rel="stylesheet">
<style>
:root{
  --bg:#c9c9c9;
  --paper:#ffffff;
  --purple:#6b449b;
  --purple-deep:#5b2f8f;
  --purple-panel:#7a2e97;
  --pink:#e0307e;
  --pink-bright:#e8307f;
  --ink:#4a4a4a;
  --white:#ffffff;
}
*{margin:0;padding:0;box-sizing:border-box}
html,body{width:1200px;height:919px;overflow:hidden;background:var(--bg);font-family:"Raleway",sans-serif}
.brochure{position:absolute;left:68px;top:78px;width:1058px;height:748px;box-shadow:0 2px 6px rgba(0,0,0,.25);display:flex}
.page-left{position:relative;width:528px;height:748px;background:linear-gradient(#fff,#f2f2f2 60%,#e6e6e6);overflow:hidden}
.panel-services{position:relative;width:266px;height:748px;background:var(--pink-bright);color:var(--white)}
.panel-testimonial{position:relative;width:264px;height:748px;background:var(--purple-panel);color:var(--white);overflow:hidden}
.abs{position:absolute}
.section-title{font-weight:700;font-size:19px;letter-spacing:.2px;display:flex;align-items:center;gap:6px;padding-bottom:3px}
.section-title .dot{width:10px;height:10px;border-radius:50%;background:currentColor;display:inline-block}
.page-left .section-title{color:var(--purple);border-bottom:1px solid var(--purple)}
.body-copy{font-size:11.2px;line-height:13.6px;color:var(--ink);text-align:justify}
.benefits-bar{left:44px;top:384px;width:435px;height:31px;background:linear-gradient(90deg,var(--purple-deep),#5a4aa0);color:#fff;font-weight:700;font-size:18px;text-align:center;line-height:31px}
.benefits-grid{left:44px;top:420px;width:435px;height:201px;background:var(--pink);display:grid;grid-template-columns:1fr 1fr;grid-template-rows:103px 1fr;color:#fff}
.benefit{padding:8px 13px;font-size:11px;line-height:13.6px;text-align:justify}
.benefit h3{font-size:15px;font-weight:700;line-height:15px;margin-bottom:2px;text-align:left}
.benefit:nth-child(1){border-right:1px dashed rgba(255,255,255,.8);border-bottom:1px dashed rgba(255,255,255,.8)}
.benefit:nth-child(2){border-bottom:1px dashed rgba(255,255,255,.8);padding-top:20px}
.benefit:nth-child(3){border-right:1px dashed rgba(255,255,255,.8)}
.panel-services .section-title,.panel-testimonial .section-title{border-bottom:1px solid #fff;color:#fff}
.services-copy{font-size:11.6px;line-height:12.6px;text-align:justify;font-weight:500}
.service-list{list-style:none;font-size:12px;line-height:17.6px}
.service-list li{padding-left:19px;position:relative}
.service-list li::before{content:"";position:absolute;left:2px;top:6px;width:7px;height:7px;border-radius:50%;background:#fff}
.service-list .sub{font-family:"Roboto Condensed",sans-serif;font-size:11.5px;padding-left:19px;line-height:17.6px}
.call{left:18px;top:688px;font-weight:700}
.call .phone{font-size:23px;line-height:26px}
.call .web{font-size:16.5px;line-height:20px}
.quote{left:24px;width:220px;font-size:9.6px;line-height:12.3px;color:#f2e6f6}
.quote::before{content:"\201C";color:#ea5aa0;font-size:18px;position:absolute;left:-10px;top:-4px;font-family:Georgia,serif}
.quote .q-end{color:#ea5aa0;font-family:Georgia,serif;font-size:16px;line-height:0}
.quote .sig{font-family:"Great Vibes",cursive;font-size:15px;color:#fff;margin-top:4px;line-height:16px}
.quote .role{font-size:8.5px;color:#e6d6ee}
.brand-name{left:0;width:264px;top:650px;text-align:center;font-family:"Raleway",sans-serif;font-weight:600;font-size:20px;color:#fff}
</style>
</head>
<body>
<div class="brochure">

  <section class="page-left">
    <svg class="abs" style="left:0;top:0" width="528" height="290" viewBox="0 0 528 290">
      <defs>
        <linearGradient id="teamTone" x1="0" y1="0" x2="1" y2="0">
          <stop offset="0" stop-color="#c9a58f"/><stop offset=".5" stop-color="#d9c2b8"/><stop offset="1" stop-color="#b48f7a"/>
        </linearGradient>
      </defs>
      <path d="M0 30 L528 30 L528 275 Q300 270 120 230 Q40 205 0 170 Z" fill="url(#teamTone)" role="img" aria-label="Photo of a smiling, diverse group of healthcare staff"/>
      <path d="M0 170 Q40 205 120 230 Q300 270 528 275 L528 290 Q300 285 110 245 Q40 225 0 185 Z" fill="var(--purple)"/>
    </svg>

    <h2 class="section-title abs" style="left:44px;top:268px;width:438px"><span class="dot"></span>ABOUT US</h2>
    <p class="body-copy abs" style="left:43px;top:295px;width:440px">Calm Fern Healthcare is a staffing provider with a contemporary approach to recruiting and placing exceptional people in human services. We maintain a comprehensive database of General Registered Nurses, Enrolled Nurses, Nursing Assistants, Medication Competent Nursing Assistants, Chefs, Cooks, Catering Assistants, Kitchen hands, Laundry and Cleaning staff. Our staff are skilled in Aged Care, Disability Services, Community Care, Public and Private Healthcare.</p>

    <div class="benefits-bar abs">KEY PARTNERSHIP BENEFITS</div>
    <div class="benefits-grid abs">
      <div class="benefit"><h3>Financial</h3>A Partnership with Calm Fern will enhance your margins &amp; profitable allowing you to put more money towards initiatives that enables operational excellence.</div>
      <div class="benefit"><h3>Risk Management Enhancements</h3>You have the option of outsourcing workcover and cost.</div>
      <div class="benefit"><h3>Service Delivery Improvements</h3>Enhanced customer choice and flexibility as well as improved customer outcomes.</div>
      <div class="benefit"><h3>Operational Efficiencies</h3>Improved organisational efficiencies and optimisation of the workforce.</div>
    </div>

    <h2 class="section-title abs" style="left:44px;top:630px;width:438px"><span class="dot"></span>WHAT WE BELIVE</h2>
    <p class="body-copy abs" style="left:42px;top:661px;width:442px;text-align:left">A Person who is appreciated, always does more than what is expected. Our staff are at the centre of all our decisions as we are only as good as people we hire. If we look after our staff, they will look after our client.</p>

    <svg class="abs" style="left:0;top:680px" width="528" height="68" viewBox="0 0 528 68">
      <path d="M0 0 Q30 35 120 52 Q300 72 528 62 L528 68 L0 68 Z" fill="var(--purple)"/>
    </svg>
  </section>

  <section class="panel-services">
    <h2 class="section-title abs" style="left:24px;top:24px;width:212px"><span class="dot"></span>SERVICES</h2>
    <p class="services-copy abs" style="left:24px;top:58px;width:212px">Our mission is to supply values driven, responsive, conscientious, &amp; responsible personnel to the aged care sector, disability services, private and public health sectors. Our passion for human services &amp; experience in recruitment, enables us to attract exceptional people with great values ready and willing to make a difference to the lives of vulnerable people.</p>
    <p class="services-copy abs" style="left:24px;top:194px;width:212px;text-align:left">We have a comprehensive database of the following personnel</p>
    <ul class="service-list abs" style="left:24px;top:225px;width:236px">
      <li>Registered Nurses</li>
      <li class="sub" style="list-style:none">(Aged Care, Disability, Emergency, Public</li>
      <li class="sub" style="list-style:none">&amp;Private healthcare)</li>
      <li>Clinical Nurses</li>
      <li>Nurse Practitioners</li>
      <li>Enrolled Nurses</li>
      <li>Assistants in Nursing (Carers/ PCA's)</li>
      <li>Support Workers</li>
      <li class="sub">(Disability, Community &amp; Mental health)</li>
      <li>Healthcare Endorsed Chefs &amp; Cooks</li>
      <li>Catering Assistants</li>
      <li>Kitchen hands</li>
      <li>Cleaners</li>
    </ul>
    <svg class="abs" style="left:27px;top:464px" width="210" height="210" viewBox="0 0 210 210">
      <circle cx="105" cy="105" r="104" fill="#7f9a6e" role="img" aria-label="Photo of a smiling young carer in a blue uniform"/>
    </svg>
    <div class="call abs">
      <div class="phone">Call Us 08 5550 1234</div>
      <div class="web">calmfernhealthcare.com.au</div>
    </div>
  </section>

  <section class="panel-testimonial">
    <h2 class="section-title abs" style="left:24px;top:24px;width:230px"><span class="dot"></span>TESTIMONIAL</h2>
    <div class="quote abs" style="top:72px">Lorem ipsum, or lipsum as it is sometimes known, is dummy text used in laying out print, graphic or web designs. The passage is attributed to an unknown typesetter in the 15th century who is thought to have <span class="q-end">&#8221;</span>
      <div class="sig">Jane Porter</div><div class="role">President</div></div>
    <div class="quote abs" style="top:181px">Lorem ipsum, or lipsum as it is sometimes known, is dummy text used in laying out print, graphic or web designs. The is <span class="q-end">&#8221;</span>
      <div class="sig">Martin D. Avery</div><div class="role">Ceo</div></div>
    <div class="quote abs" style="top:267px">Lorem ipsum, or lipsum as it is sometimes known, is dummy text used in laying out print, graphic or web designs. The is <span class="q-end">&#8221;</span>
      <div class="sig">Lena G. Cortez</div><div class="role">Managing Director</div></div>
    <svg class="abs" style="left:0;top:340px" width="264" height="408" viewBox="0 0 264 408">
      <defs>
        <linearGradient id="elderTone" x1="0" y1="0" x2="1" y2="1">
          <stop offset="0" stop-color="#8a6a58"/><stop offset=".55" stop-color="#2f6a5e"/><stop offset="1" stop-color="#3b3f44"/>
        </linearGradient>
      </defs>
      <path d="M0 10 Q130 -5 225 100 Q255 140 264 170 L264 408 L0 408 Z" fill="url(#elderTone)" role="img" aria-label="Photo of a smiling elderly woman in a wheelchair"/>
      <path d="M0 0 Q130 -15 232 90 Q258 125 264 150 L264 170 Q255 140 225 100 Q130 -5 0 10 Z" fill="var(--purple)"/>
    </svg>
    <div class="brand-name abs">Calm Fern Healthcare</div>
  </section>

</div>
</body>
</html>
```